Vintage poster/postcard for 2011 New Years Eve event with theme 'Lumière Volante'

I have had a major change of mind since the last brief due to my original requirements being too specific. I hope this new brief allows more scope for the designers and I am extending the deadline by 7 days.

For the first time my new business 'Tidewell Gala' is planning an exciting, large scale New Years Eve fundraising event in Hobart Tasmania, Australia. The unique and eclectic theme of the party is 'Lumière Volante' (french for contemporary circus). I require a vintage style poster design (similar to a traditional french advertising poster) that can double as a postcard invitation so it must look good on a smaller scale as well.
Updates

Project Deadline Extended
Reason: My original brief was very specific and I now realise very limiting for the designers. I have changed my mind with the look I want for the vintage poster (more along the lines of the traditional french advertising posters of old) and therefore would like to allow designers extra time to submit a design. Thank you. Jill Barrow Tidewell Gala

Target Market(s)

25-50 yr old professionals prepared to pay premium price for a quality, fresh & fun NYE experience while giving to charity.

Industry/Entity Type

Advertising

Requirements
Must have
• - A heading that reads: Tidewell Gala proudly presents
Lumière Volante
- Text that includes: 2011 New Years Eve Extravanaganza Saturday 31st December and find out more at "www.tidewellgala.example
- A strip left blank at the bottom to include my business logo and others sponsors
- Classic french vintage poster design
- - Plenty of colour but not too fluro
- Something that looks good enough to be framed or sent to a friend
Should not have
• - Picture of Eiffel Tower or any other specific French references
- Any animals

```html
<!DOCTYPE html>
<html lang="en">
<head>
<meta charset="utf-8">
<title>Tidewell Gala – Lumière Volante New Years Eve 2011</title>
<link rel="stylesheet" href="https://fonts.googleapis.com/css2?family=Jost:wght@500;700;800&display=swap">
<style>
  :root {
    --night: #1c2a12;
    --forest: #2f5a23;
    --meadow: #4f9a4a;
    --sage: #8fc47a;
    --lime: #c4e02a;
    --olive-ink: #4c5a10;
    --lavender: #cfb6e0;
    --lavender-pale: #e6d8ef;
    --plum: #3a1e45;
    --teal-ink: #2e6a4a;
    --white: #ffffff;
  }
  * { margin: 0; padding: 0; box-sizing: border-box; }
  html, body { width: 816px; height: 1200px; overflow: hidden; background: var(--night); }
  .poster {
    position: relative; width: 816px; height: 1200px; overflow: hidden;
    font-family: "Jost", "Century Gothic", sans-serif; font-weight: 800;
    text-transform: uppercase;
  }
  .backdrop { position: absolute; inset: 0; }
  .tilted {
    position: absolute; inset: 0;
    transform: rotate(-14deg); transform-origin: 408px 560px;
  }
  .tilted > *, .tilted h1 > * { position: absolute; white-space: nowrap; line-height: 1; }
  .artwork {
    left: 60px; top: 440px; width: 500px; height: 340px;
    border-radius: 50% 45% 40% 50%;
    background: radial-gradient(ellipse at 50% 45%, #8a9a14 0%, #56620e 55%, #2e3709 100%);
  }
  .headline { left: 140px; top: 190px; color: var(--white); font-size: 32px; }
  .headline .soft { color: var(--lime); font-weight: 700; text-transform: none; }
  .box { box-shadow: 0 6px 18px rgba(0,0,0,0.35); }
  .title-small {
    left: 130px; top: 236px; padding: 10px 16px 6px;
    background: var(--lime); color: var(--olive-ink); font-size: 54px;
  }
  .title-big {
    left: 100px; top: 300px; width: 600px; height: 132px; padding-top: 14px;
    text-align: center;
    background: linear-gradient(180deg, var(--lavender-pale), var(--lavender));
    color: var(--plum); font-size: 106px; letter-spacing: -2px;
  }
  .day {
    right: 116px; top: 442px; padding: 8px 16px 6px;
    background: var(--lavender); color: var(--teal-ink); font-size: 50px;
  }
  .date {
    right: 116px; top: 510px; padding: 8px 16px 6px;
    background: var(--lavender-pale); color: var(--plum); font-size: 50px;
  }
  .date sup { font-size: 28px; vertical-align: 14px; }
  .year {
    right: 126px; top: 582px; color: var(--lime);
    font-size: 80px; text-shadow: 0 3px 8px rgba(0,0,0,0.4);
  }
  .occasion {
    right: 126px; top: 670px; color: var(--lime);
    font-size: 42px; text-shadow: 0 3px 8px rgba(0,0,0,0.4);
  }
  .extravaganza {
    left: 150px; top: 724px; padding: 10px 16px 6px;
    background: var(--lavender-pale); color: var(--plum); font-size: 50px;
  }
  .find-out { left: 0; width: 816px; text-align: center; top: 836px; color: var(--white); font-size: 30px; }
  .web {
    left: 0; width: 816px; text-align: center; top: 880px;
    color: var(--white); font-size: 40px; text-transform: lowercase;
  }
  .web .accent { color: var(--sage); }
  .sponsor-strip { position: absolute; left: 0; right: 0; bottom: 0; height: 150px; }
</style>
</head>
<body>
<main class="poster">
  <svg class="backdrop" width="816" height="1200" viewBox="0 0 816 1200" aria-hidden="true">
    <defs>
      <radialGradient id="vignette" cx="50%" cy="50%" r="70%">
        <stop offset="0" stop-color="#5a7a2a"/>
        <stop offset="0.7" stop-color="#2f4418"/>
        <stop offset="1" stop-color="#151f0c"/>
      </radialGradient>
      <radialGradient id="disc" cx="55%" cy="40%" r="60%">
        <stop offset="0" stop-color="#a6d79a"/>
        <stop offset="0.6" stop-color="#4f9a4a"/>
        <stop offset="1" stop-color="#2f5a23"/>
      </radialGradient>
    </defs>
    <rect width="816" height="1200" fill="url(#vignette)"/>
    <ellipse cx="420" cy="580" rx="520" ry="560" transform="rotate(-20 420 580)" fill="url(#disc)"/>
    <polygon points="0,620 816,240 816,400 0,860" fill="#c8e030" opacity="0.9"/>
    <polygon points="0,1040 816,900 816,1070 0,1200" fill="#1c2a12" opacity="0.55"/>
  </svg>

  <div class="tilted">
    <div class="artwork" role="img" aria-label="Theatrical circus mask illustration in olive and lime tones"></div>

    <p class="headline">Tidewell Gala <span class="soft">proudly presents</span></p>
    <h1>
      <span class="box title-small">Lumière</span>
      <span class="box title-big">Volante</span>
    </h1>
    <p class="box day">Saturday</p>
    <p class="box date">31<sup>st</sup> December</p>
    <p class="year">2011</p>
    <p class="occasion">New Years Eve</p>
    <p class="box extravaganza">Extravanaganza</p>
    <p class="find-out">Find out more at</p>
    <p class="web">www.<span class="accent">tidewellgala</span>.example</p>
  </div>

  <div class="sponsor-strip" aria-hidden="true"></div>
</main>
</body>
</html>
```